Flyer-Design für psychologische Beratung und Therapie
Zielgruppe
In meiner Praxis für psychologische Beratung und Therapie unterstütze ich Menschen dabei, ihre Probleme zu lösen. Schwerpunkte sind die Stärkung des Selbstwertgefühls, Überwindung von Ängsten und Krisen.
Aufgabenstellung
Din lang 4-Seitig
(Zitat)
'Bei aller Ernsthaftigkeit und Empathie dürfen Leichtigkeit,
Zuversicht und Humor in der Therapie nicht zu kurz kommen.“
(Text)
Mein Name ist Karl Ewald Lambrecht, ich bin Transaktionsanalytiker, psychotherapeutischer Heilpraktiker und begeisterter VKT® Therapeut. Wenn Sie zufriedener leben wollen, neue Wege einschlagen oder sich beruflich oder persönlich weiterentwickeln wollen, begleite ich Sie gern dabei!
Möchten Sie ein stärkeres Selbstwertgefühl entwickeln, Ängste reduzieren oder eine akute Krise überwinden? Oder geeignete Strategien entwickeln, damit Sie Ihren Beruf zufriedener und erfolgreicher ausüben können? Auf dem Weg zu Ihrem Ziel biete ich Ihnen Unterstützung, vereinbaren Sie gerne einen ersten Termin!

```html
<!DOCTYPE html>
<html lang="de">
<head>
<meta charset="utf-8">
<title>Psychologische Beratung und Therapie – Flyer</title>
<link rel="stylesheet" href="https://fonts.googleapis.com/css2?family=Jost:wght@300;400&family=Open+Sans:wght@400;600;700;800&display=swap">
<style>
  :root {
    --paper: #ffffff;
    --orange: #f39a1e;
    --amber: #f0a81e;
    --band: #f2b61a;
    --grey-text: #5c5c5c;
    --grey-logo: #8a8a8a;
    --ink: #111111;
    --rule: #cfcfcf;
  }
  * { margin: 0; padding: 0; box-sizing: border-box; }
  html, body { width: 1200px; height: 1200px; overflow: hidden; background: var(--paper); }
  .flyer { position: relative; width: 1200px; height: 1200px; background: var(--paper); font-family: "Open Sans", sans-serif; }

  /* Back panel (left) */
  .contact-call {
    position: absolute; left: 0; width: 600px; top: 802px;
    text-align: center; font-size: 25px; font-weight: 600; color: var(--grey-text);
  }
  .contact-divider { position: absolute; top: 883px; left: 95px; width: 410px; height: 62px; }
  .contact-name {
    position: absolute; left: 0; width: 600px; top: 990px;
    text-align: center; font-size: 20px; font-weight: 700; color: var(--amber);
  }
  .contact-details {
    position: absolute; left: 0; width: 600px; top: 1034px;
    text-align: center; font-size: 16.5px; line-height: 24.5px; color: var(--grey-text);
  }
  .contact-details b { color: var(--ink); font-weight: 700; }

  /* Cover panel (right) */
  .brand { position: absolute; left: 640px; top: 82px; }
  .brand-dot { position: absolute; left: 0; top: 4px; width: 68px; height: 68px; border-radius: 50%; background: var(--orange); }
  .brand-name {
    position: absolute; left: 103px; top: 0; white-space: nowrap;
    font-family: "Jost", sans-serif; font-weight: 400; font-size: 38px; letter-spacing: 0.5px; color: var(--grey-logo);
  }
  .brand-tagline {
    position: absolute; left: 104px; top: 44px; white-space: nowrap;
    font-family: "Jost", sans-serif; font-weight: 300; font-size: 25.5px; color: var(--orange);
  }
  .brand-rule { position: absolute; left: 672px; top: 200px; width: 455px; height: 1px; background: var(--rule); }
  .cover-photo {
    position: absolute; left: 656px; top: 260px; width: 482px; height: 678px;
    background: linear-gradient(180deg, #f6f1e6 0%, #efe6cf 40%, #d9a77c 62%, #b77a4d 80%, #8d5a35 100%);
  }
  .cover-band {
    position: absolute; left: 641px; top: 915px; width: 518px; height: 180px;
    background: var(--band); color: #fff; text-align: center;
    display: flex; align-items: center; justify-content: center; padding-top: 8px;
  }
  .cover-title { font-size: 40px; font-weight: 800; line-height: 47px; }
</style>
</head>
<body>
<main class="flyer">

  <section class="back-panel">
    <p class="contact-call">Sprechen Sie mich gerne an!</p>
    <svg class="contact-divider" viewBox="0 0 410 62" aria-hidden="true">
      <line x1="0" y1="32" x2="138" y2="32" stroke="var(--rule)" stroke-width="1.5"/>
      <line x1="272" y1="31" x2="410" y2="31" stroke="var(--rule)" stroke-width="1.5"/>
      <circle cx="206" cy="31" r="31" fill="var(--orange)"/>
      <path d="M196 20c1.5-1.3 3-1 4 .5l2.6 4c.8 1.3.4 2.5-.6 3.3l-1.4 1.1c1 2.6 3.2 5 5.8 6.3l1.2-1.4c.9-1 2.1-1.3 3.3-.5l4 2.7c1.4 1 1.6 2.6.3 4l-1.6 1.6c-2 2-6 1.2-10.3-2.2-4.2-3.3-7.8-8-8.8-11.8-.6-2.5-.1-4.6 1.5-6z" fill="#fff"/>
    </svg>
    <h2 class="contact-name">Karl Ewald Lambrecht</h2>
    <p class="contact-details">
      <b>Adresse</b> Lindenweg 7, 24999 Musterfelde<br>
      <b>Telefon</b> 04399 123456<br>
      <b>Web</b> www.praxis-lambrecht-demo.de
    </p>
  </section>

  <section class="cover-panel">
    <div class="brand">
      <span class="brand-dot"></span>
      <span class="brand-name">KARL EWALD LAMBRECHT</span>
      <span class="brand-tagline">Psychologische Beratung &amp; Therapie</span>
    </div>
    <div class="brand-rule"></div>
    <div class="cover-photo" role="img" aria-label="Foto: einander haltende Hände auf einem Holztisch vor hellem, unscharfem Hintergrund"></div>
    <div class="cover-band">
      <h1 class="cover-title">Psychologische<br>Beratung und Therapie</h1>
    </div>
  </section>

</main>
</body>
</html>
```